Bookcover: Lessons From the Silent Orchard

I am publishing a super-low-cost innovation book for €4,99 on Bravolo Self Release to help everyone become a great innovator: young ambitious people without college education nor a big budget. Do you want to help me?

Brief:
Design a book cover 1600 x 2560 pixels for BSR.
Main title: Lessons From the Silent Orchard
Sub title: mindset - insights - skills & tools
Author: Maarten de Klerk
Design: captive, and appealing to everyone
Target Group: young ambitious people without college education

For bravolo please format the height/width ratio of 1.6:1

```html
<!DOCTYPE html>
<html lang="en">
<head>
<meta charset="utf-8">
<title>Lessons From the Silent Orchard — Book Cover</title>
<link rel="stylesheet" href="https://fonts.googleapis.com/css2?family=Lato:wght@400;900&display=swap">
<style>
  :root {
    --backdrop: #e2e2e2;
    --orange-left: #e0552a;
    --orange-right: #f09b27;
    --orange-deep: #c43a12;
    --stair-black: #1a1a1a;
    --stair-soft: #3a2218;
    --band-purple: #661266;
    --band-blue: #2b9ddc;
    --band-indigo: #433e80;
    --band-green: #00944a;
    --ink-white: #ffffff;
  }
  * { margin: 0; padding: 0; box-sizing: border-box; }
  html, body {
    width: 1170px; height: 1200px; overflow: hidden;
    background: var(--backdrop);
    font-family: "Lato", Arial, sans-serif;
  }
  .book-cover {
    position: absolute; left: 243px; top: 52px;
    width: 684px; height: 1095px; overflow: hidden;
    background:
      linear-gradient(180deg, rgba(196,58,18,0) 28%, rgba(196,58,18,0.75) 100%),
      linear-gradient(90deg, var(--orange-left) 0%, var(--orange-left) 25%, var(--orange-right) 75%);
  }
  .staircase-art {
    position: absolute; inset: 0;
    clip-path: polygon(642px 176px, 684px 176px, 684px 1095px, 0 1095px, 0 1070px);
    background: linear-gradient(160deg, var(--stair-soft) 0%, var(--stair-black) 45%, var(--stair-black) 100%);
  }
  .climber-art {
    position: absolute; left: 123px; top: 495px; width: 175px; height: 442px;
    border-radius: 60px 60px 20px 20px;
    background: linear-gradient(180deg, #f5c020 0%, #f2f2f2 45%, #1a1a1a 100%);
    opacity: 0.9;
  }
  .title { position: absolute; left: 0; top: 43px; }
  .title-band {
    display: block; width: max-content; height: 76px; margin-bottom: 12px;
    padding: 0 12px 0 43px;
    color: var(--ink-white); font-weight: 900; font-size: 80px;
    line-height: 80px; letter-spacing: -1px; text-transform: uppercase;
  }
  .band-purple { background: var(--band-purple); }
  .band-blue { background: var(--band-blue); }
  .band-indigo { background: var(--band-indigo); }
  .band-green { background: var(--band-green); }
  .subtitle {
    position: absolute; left: 451px; top: 788px;
    color: var(--ink-white); font-weight: 900; font-size: 43px;
    line-height: 49px; letter-spacing: -0.5px; list-style: none;
  }
  .author {
    position: absolute; left: 364px; top: 1032px;
    color: var(--ink-white); font-weight: 400; font-size: 35px; line-height: 1;
  }
</style>
</head>
<body>
  <main class="book-cover">
    <div class="staircase-art" role="img" aria-label="Illustration of a black staircase rising diagonally from bottom left to top right"></div>

    <div class="climber-art" role="img" aria-label="Illustration of a young man with a yellow backpack climbing the stairs, seen from behind"></div>

    <h1 class="title">
      <span class="title-band band-purple">Lessons</span>
      <span class="title-band band-blue">From the</span>
      <span class="title-band band-indigo">Silent</span>
      <span class="title-band band-green">Orchard</span>
    </h1>

    <ul class="subtitle">
      <li>MINDSET</li>
      <li>INSIGHTS</li>
      <li>SKILLS</li>
      <li>&amp; TOOLS</li>
    </ul>

    <p class="author">Maarten de Klerk</p>
  </main>
</body>
</html>
```